Webdesign für Bedrucken Papiertaschen, Schildern etc.
Zielgruppe
Wir bedrucken Papiertaschen, Papierbeutel, Laternen, Aluplaketten, Schilder, etc. und lasern Hundemarken. Zielgruppen von Privat bis Geschäftskunden
Aufgabenstellung
Der Shop sollte ein einfacher und kostengünstiger 'web2print'-shop werden. Wo die Kunden anhand von einem Editor Ihre Logos oder Druckvorlagen selber hochladen und/oder gestalten könne. Bisher haben die Kunden eifach ihre Bidldatei per E-Mail geschickt und wir haben diese dann weiter verarbeit.
Der Shop sollte, wenn möglich, günstig im Unterhalt sein, da wir nicht abschätzen können, wie gut diese laufen wird.
Wir haben wie 3 Bereich: 1. Papierbeutel/Taschen / 2. Stallplaketten (für z.B. Pferdesport) / 3. Diverses (Wie z.B. die Laternen, Schilder, Hundemarken, etc.)
Es würde sich um eine separate Webseite handeln. Daher ist bei Design freie Hand, eifach und klar... auch für nicht so ambitionierte Privatkunden oder kleine Unternehmen.

```html
<!DOCTYPE html>
<html lang="de">
<head>
<meta charset="utf-8">
<title>Faltenbeutel braun – Tütenwerk</title>
<link href="https://fonts.googleapis.com/css2?family=Inter:wght@400;500;600&family=Inter+Tight:wght@600;700;800&family=JetBrains+Mono:wght@400;500&display=swap" rel="stylesheet">
<style>
:root{
  --red:#d92b1e;
  --ink:#111111;
  --muted:#6b6b6b;
  --line:#dedbd5;
  --bg:#f6f6f4;
  --band:#efeeea;
  --white:#ffffff;
  --black:#070707;
  --kraft:#c9a877;
}
*{box-sizing:border-box;margin:0;padding:0}
html,body{width:988px;height:1200px;overflow:hidden}
body{position:relative;background:var(--bg);font-family:"Inter",sans-serif;color:var(--ink);font-size:10px}
.mono{font-family:"JetBrains Mono",monospace}
.abs{position:absolute}

/* top bar */
.topbar{left:0;top:0;width:988px;height:20px;background:var(--black);color:#eee;display:flex;align-items:center;justify-content:space-between;padding:0 38px;font-size:7.5px;letter-spacing:.4px}
.topbar .dot{display:inline-block;width:4px;height:4px;border-radius:50%;background:var(--red);margin-right:4px;vertical-align:middle}

/* header */
.header{left:0;top:20px;width:988px;height:56px;background:var(--white);border-bottom:1px solid var(--line)}
.brand{display:flex;align-items:center;gap:6px;font-family:"Inter",sans-serif;font-weight:600;font-size:12px}
.brand .mark{width:10px;height:10px;background:var(--red);display:block}
.header .brand{left:38px;top:21px;color:var(--ink)}
.nav{left:207px;top:21px;display:flex;gap:19px;font-size:10.3px}
.nav a{color:var(--ink);text-decoration:none;padding-bottom:4px}
.nav a.active{border-bottom:1.5px solid var(--red)}
.iconbtn{top:15px;width:25px;height:25px;border:1px solid var(--line);border-radius:50%;display:flex;align-items:center;justify-content:center}
.cart{left:842px;top:14px;width:108px;height:27px;border-radius:14px;background:var(--red);color:#fff;display:flex;align-items:center;justify-content:center;gap:6px;font-weight:600;font-size:10px}
.cart .count{width:13px;height:13px;border-radius:50%;background:#fff;color:var(--red);font-size:7px;display:flex;align-items:center;justify-content:center}

.crumbs{left:38px;top:85px;font-size:8.8px;color:var(--muted);display:flex;gap:9px}
.crumbs .cur{color:var(--ink)}

.photo{left:39px;top:114px;width:435px;height:435px;border-radius:8px;background:linear-gradient(135deg,#e9e4dc 0%,#c8a67a 35%,#b48f62 60%,#2a2724 100%)}

/* product */
.badge{left:513px;top:114px;height:16px;padding:0 7px;border-radius:8px;background:var(--red);color:#fff;font-size:7px;display:flex;align-items:center;letter-spacing:.4px}
.artnr{left:584px;top:118px;font-size:7.5px;color:var(--muted);letter-spacing:.5px}
.title{left:512px;top:136px;font-family:"Inter Tight",sans-serif;font-weight:700;font-size:47px;letter-spacing:-2.2px;line-height:52px;white-space:nowrap}
.desc{left:513px;top:191px;width:372px;font-size:10.3px;line-height:17.2px}
.lbl{font-size:7.5px;letter-spacing:.6px;color:var(--muted)}
.row{left:513px;width:436px;display:flex;gap:6px}
.opt{background:#fff;border:1px solid var(--line);border-radius:6px;flex:1}
.opt.on{background:var(--red);border-color:var(--red);color:#fff}
.opt.on .mono{color:#ffd4cf}
.fmt{height:50px;padding:10px 9px}
.fmt b{font-size:12px;font-weight:600;display:block}
.fmt .mono{font-size:6.8px;color:var(--muted);margin-top:5px;display:block}
.sw{flex:none;height:30px;padding:0 10px 0 7px;display:flex;align-items:center;gap:7px;font-size:9.3px}
.sw.on{background:#fff;color:var(--red);border:1.5px solid var(--red)}
.sw i{width:15px;height:15px;border-radius:50%;border:1px solid var(--line);display:block}
.dr{height:51px;padding:9px 10px;display:flex;flex-direction:column;justify-content:center}
.dr b{font-size:9.5px;font-weight:600}
.dr .mono{font-size:6.5px;color:var(--muted);margin-top:4px;line-height:9.5px}
.qty{height:37px;text-align:center;display:flex;flex-direction:column;justify-content:center;gap:3px}
.qty b{font-size:10px;font-weight:600}
.qty .mono{font-size:6.5px;color:var(--muted)}

.summary{left:513px;top:567px;width:436px;height:143px;background:#fff;border:1px solid var(--line);border-radius:9px}
.sumline{left:16px;width:220px;display:flex;justify-content:space-between;font-size:8.8px}
.sumline .mono{font-size:8.8px}
.total{left:16px;top:80px;width:220px;display:flex;justify-content:space-between;align-items:center}
.total span{font-size:8.8px}
.total b{font-family:"Inter Tight",sans-serif;font-size:25px;font-weight:700;letter-spacing:-.8px}
.editor{left:259px;top:16px;width:162px;height:40px;border-radius:20px;background:var(--red);color:#fff;display:flex;align-items:center;justify-content:center;gap:8px;font-weight:600;font-size:10.5px}
.upload{left:259px;top:73px;width:162px;text-align:center;font-size:9.8px;font-weight:600}
.ship{left:259px;top:105px;width:162px;text-align:center;font-size:7px;line-height:10.5px;color:var(--ink)}

/* technical data */
.tech{left:0;top:738px;width:988px;height:214px;background:var(--band);border-top:1px solid var(--line)}
.tech h2{position:absolute;left:38px;top:55px;font-family:"Inter Tight",sans-serif;font-weight:700;font-size:25px;line-height:27px;letter-spacing:-.8px}
.tech .lbl{position:absolute;left:38px;top:41px}
.spec{position:absolute;width:281px;height:56px;border-bottom:1px solid var(--line)}
.spec .lbl{position:static;display:block;margin-bottom:5px;font-size:7px}
.spec p{font-size:10.3px}

/* footer */
.footer{left:0;top:952px;width:988px;height:248px;background:var(--black);color:#f2f2f2}
.footer .brand{position:absolute;left:38px;top:34px;color:#f2f2f2;font-size:11px}
.fabout{position:absolute;left:38px;top:75px;width:215px;font-size:8.8px;line-height:14.4px}
.fcol{position:absolute;top:33px}
.fcol h4{font-size:9.3px;font-weight:600;letter-spacing:.6px;margin-bottom:12px}
.fcol a{display:block;color:#f2f2f2;text-decoration:none;font-size:8.8px;line-height:17.8px}
.fline{position:absolute;left:38px;top:203px;width:912px;height:1px;background:#2a2a2a}
.fbottom{position:absolute;left:38px;top:218px;width:912px;display:flex;justify-content:space-between;font-size:7.8px}
.fbottom .pay{display:flex;gap:12px}
</style>
</head>
<body>

<div class="abs topbar mono">
  <span><span class="dot"></span>VERSAND CH AB CHF 9.50 — DE/FR/IT VERFÜGBAR</span>
  <span>DRUCK IN 3-5 WERKTAGEN · LASERGRAVUR AB 24 H</span>
  <span>HILFE? +41 44 000 12 34</span>
</div>

<header class="abs header">
  <div class="abs brand"><span class="mark"></span>Tütenwerk</div>
  <nav class="abs nav">
    <a class="active" href="#">Papierbeutel &amp; Taschen</a>
    <a href="#">Stallplaketten</a>
    <a href="#">Hundemarken &amp; Diverses</a>
    <a href="#">Über uns</a>
    <a href="#">Hilfe</a>
  </nav>
  <div class="abs iconbtn" style="left:768px">
    <svg width="10" height="10" viewBox="0 0 10 10" fill="none" stroke="#111" stroke-width="1.2"><circle cx="4.3" cy="4.3" r="3.2"/><path d="M6.6 6.6 9 9"/></svg>
  </div>
  <div class="abs iconbtn" style="left:805px">
    <svg width="10" height="10" viewBox="0 0 10 10" fill="none" stroke="#111" stroke-width="1.1"><circle cx="5" cy="3.2" r="2"/><path d="M1.5 9.3c.5-2.2 1.8-3.2 3.5-3.2s3 1 3.5 3.2"/></svg>
  </div>
  <div class="abs cart">
    <svg width="10" height="10" viewBox="0 0 10 10" fill="none" stroke="#fff" stroke-width="1.1"><path d="M.5 1h1.5l1.2 5.5h5l1-4H2.5"/><circle cx="3.8" cy="8.6" r=".7"/><circle cx="7.6" cy="8.6" r=".7"/></svg>
    Warenkorb <span class="count">0</span>
  </div>
</header>

<div class="abs crumbs">
  <span>Sortiment</span><span>›</span><span>Papierbeutel &amp; Taschen</span><span>›</span><span class="cur">Faltenbeutel braun, WaldPlus</span>
</div>

<div class="abs photo" role="img" aria-label="Produktfoto: gestapelte braune Papierfaltenbeutel mit aufgedrucktem Kundenlogo"></div>

<div class="abs badge mono">BESTSELLER</div>
<div class="abs artnr mono">ART.-NR. PFB-7126</div>
<h1 class="abs title">Faltenbeutel braun</h1>
<p class="abs desc">Klassischer Papierfaltenbeutel aus 70 g/m² Kraftpapier, WaldPlus-zertifiziert. Ideal für Bäckereien, Take-Away, Geschenke und Verpackung. Bedruckung 1- bis 4-farbig, einseitig oder zweiseitig.</p>

<div class="abs lbl mono" style="left:513px;top:260px">01 / FORMAT</div>
<div class="abs lbl mono" style="left:849px;top:260px;width:100px;text-align:right">BREITE × HÖHE</div>
<div class="abs row" style="top:276px">
  <div class="opt fmt"><b>S</b><span class="mono">12 × 20 cm</span></div>
  <div class="opt fmt on"><b>M</b><span class="mono">16 × 26 cm</span></div>
  <div class="opt fmt"><b>L</b><span class="mono">20 × 30 cm</span></div>
  <div class="opt fmt"><b>XL</b><span class="mono">25 × 36 cm</span></div>
</div>

<div class="abs lbl mono" style="left:513px;top:344px">02 / PAPIERFARBE</div>
<div class="abs row" style="top:360px">
  <div class="opt sw on"><i style="background:var(--kraft);border-color:#b89466"></i>Kraft natur</div>
  <div class="opt sw"><i style="background:#fff"></i>Weiss</div>
  <div class="opt sw"><i style="background:#111;border-color:#111"></i>Schwarz</div>
</div>

<div class="abs lbl mono" style="left:513px;top:408px">03 / DRUCK</div>
<div class="abs row" style="top:424px">
  <div class="opt dr on"><b>1-farbig</b><span class="mono">Sonderfarbe · keine Klischeekosten</span></div>
  <div class="opt dr"><b>2-farbig</b><span class="mono">+ CHF 60 Klischee</span></div>
  <div class="opt dr"><b>4-farbig (CMYK)</b><span class="mono">+ CHF 120 Klischee</span></div>
</div>

<div class="abs lbl mono" style="left:513px;top:494px">04 / AUFLAGE</div>
<div class="abs lbl mono" style="left:849px;top:494px;width:100px;text-align:right">STK.-PREIS SINKT</div>
<div class="abs row" style="top:510px">
  <div class="opt qty"><b>100</b><span class="mono">0.58</span></div>
  <div class="opt qty"><b>250</b><span class="mono">0.46</span></div>
  <div class="opt qty on"><b>500</b><span class="mono">0.34</span></div>
  <div class="opt qty"><b>1’000</b><span class="mono">0.26</span></div>
  <div class="opt qty"><b>2’500</b><span class="mono">0.21</span></div>
  <div class="opt qty"><b>5’000</b><span class="mono">0.17</span></div>
</div>

<div class="abs summary">
  <div class="abs sumline" style="top:33px"><span>Stückpreis</span><span class="mono">CHF 0.34</span></div>
  <div class="abs sumline" style="top:49px"><span>Lieferung CH</span><span class="mono">CHF 12.00</span></div>
  <div class="abs total"><span>Gesamtsumme</span><b>CHF 182.00</b></div>
  <div class="abs editor">
    <svg width="11" height="11" viewBox="0 0 11 11" fill="none" stroke="#fff" stroke-width="1.1"><path d="M7.5 1.5l2 2-6 6H1.5v-2z"/></svg>
    Im Editor gestalten
  </div>
  <div class="abs upload">Druckdatei hochladen</div>
  <div class="abs ship mono">Versand in ca. 5 Werktagen ab Druckfreigabe</div>
</div>

<section class="abs tech">
  <span class="lbl mono">TECHNISCHE DATEN</span>
  <h2>Material<br>&amp; Druck.</h2>
  <div class="spec" style="left:368px;top:38px"><span class="lbl mono">MATERIAL</span><p>Kraftpapier 70 g/m², WaldPlus Mix</p></div>
  <div class="spec" style="left:668px;top:38px"><span class="lbl mono">DRUCKVERFAHREN</span><p>Flexodruck (ab 1’000), Digital (ab 100)</p></div>
  <div class="spec" style="left:368px;top:94px"><span class="lbl mono">DRUCKFLÄCHE</span><p>Vollflächig (Beschnitt 3 mm)</p></div>
  <div class="spec" style="left:668px;top:94px"><span class="lbl mono">VERSCHLUSS</span><p>Seitenfalten, offen oben</p></div>
  <div class="spec" style="left:368px;top:150px"><span class="lbl mono">LEBENSMITTELECHT</span><p>Ja, geeignet für trockene Lebensmittel</p></div>
  <div class="spec" style="left:668px;top:150px"><span class="lbl mono">VEREDELUNG</span><p>Heissprägung, Hochglanz auf Anfrage</p></div>
</section>

<footer class="abs footer">
  <div class="brand"><span class="mark"></span>Tütenwerk</div>
  <p class="fabout">Druckerei und Lasergravur aus der Schweiz. Wir bedrucken Papierbeutel, Stallplaketten, Laternen, Schilder und lasern Hundemarken — vom Einzelstück bis zur Grossauflage.</p>
  <div class="fcol" style="left:397px"><h4>PRODUKTE</h4><a>Papierbeutel</a><a>Papiertaschen</a><a>Stallplaketten</a><a>Hundemarken</a><a>Laternen &amp; Schilder</a><a>Aluplaketten</a></div>
  <div class="fcol" style="left:592px"><h4>SERVICE</h4><a>Druckvorlagen-Editor</a><a>Druckdaten anliefern</a><a>Materialmuster bestellen</a><a>Mengenrabatte</a><a>Versand &amp; Lieferung</a><a>Hilfe &amp; FAQ</a></div>
  <div class="fcol" style="left:787px"><h4>FIRMA</h4><a>Über uns</a><a>Nachhaltigkeit</a><a>Geschäftskunden</a><a>Kontakt</a><a>AGB</a><a>Impressum</a></div>
  <div class="fline"></div>
  <div class="fbottom mono">
    <span>© 2026 Tütenwerk · Rindler Pack AG · CH-8999 Seefeld / Zürich</span>
    <span class="pay"><span>Mobile Pay</span><span>Kreditkarte</span><span>Debitkarte</span><span>Rechnung</span><span>Postkonto</span></span>
  </div>
</footer>

</body>
</html>
```